"Velmora Kestrel Bridgeworks": unique end to end Chinese marketing and ecommerce solutions*

I would like to create a company website for my trademark: "Velmora Kestrel Bridgeworks". We are based in Iceland. We are the only company in the market offering end-to-end Chinese digital marketing and eCommerce solutions. We help companies grow their brands and sales towards Chinese - whether tourism, export of products or services.
I include the logo that we have come up with in terms of colours and fonts.
The font is Trajan - I would like to use normal letters (capital and lowercase) for text.
Front page: Picture with colour filter. Logo in white. Text line underneath.
I am inspired by this website:
https://www.pelorumgrove.example/
I like these short videos for landing page:
https://www.framelodex.example/video/clip-30417852-ridge-scenic-vista-mountains
https://www.framelodex.example/video/clip-2093847155-4k-aerial-video-ridge-path-vista
https://www.framelodex.example/video/clip-3058172649-ridge-path-vista
Icelandic businesses looking for business opportunities in China or to attract Chinese tourists.
Digital Marketing

```html
<!DOCTYPE html>
<html lang="en">
<head>
<meta charset="utf-8">
<title>Velmora Kestrel Bridgeworks</title>
<link href="https://fonts.googleapis.com/css2?family=Cinzel:wght@400;600;700&family=Montserrat:wght@400;500;600;700&family=Raleway:wght@400;500;600&display=swap" rel="stylesheet">
<style>
:root{
  --gold:#b5893b;
  --gold-light:#c9a25a;
  --blue:#1f5fae;
  --blue-deep:#174a8c;
  --navy:#1c3f78;
  --ink:#333a44;
  --muted:#6b717a;
  --pale:#e8eef7;
  --footer:#30363e;
  --white:#ffffff;
}
*{margin:0;padding:0;box-sizing:border-box}
html,body{width:1200px;height:4175px;overflow:hidden}
body{position:relative;background:var(--white);font-family:"Raleway",sans-serif;color:var(--ink)}
.abs{position:absolute}
.serif{font-family:"Cinzel",serif}
.sans{font-family:"Montserrat",sans-serif}

/* header */
.site-header{left:0;top:0;width:1200px;height:98px;background:linear-gradient(90deg,#f4f6fa,#e6ebf3);z-index:5}
.brand{left:48px;top:26px;display:flex;align-items:center;gap:14px}
.brand-mark{width:34px;height:34px;background:var(--gold);border-radius:50%}
.brand-name{font-family:"Cinzel",serif;font-size:24px;font-weight:600;color:var(--blue);line-height:1.05}
.call{left:664px;top:26px;display:flex;align-items:center;gap:10px}
.call-label{font-family:"Montserrat",sans-serif;font-size:13px;color:var(--blue);line-height:1.1}
.call-number{font-family:"Montserrat",sans-serif;font-size:19px;font-weight:700;color:#222}
.quote-btn{left:906px;top:28px;width:171px;height:42px;background:var(--gold);color:#fff;font-family:"Montserrat",sans-serif;font-weight:700;font-size:14px;display:flex;align-items:center;justify-content:center;gap:8px;border-radius:3px}
.menu-btn{left:1093px;top:28px;width:55px;height:42px;background:var(--blue);border-radius:3px;display:flex;flex-direction:column;justify-content:center;align-items:center;gap:5px}
.menu-btn span{width:26px;height:3px;background:#fff;display:block}

/* hero */
.hero-photo{left:0;top:98px;width:1200px;height:760px;background:linear-gradient(180deg,#3f78b0 0%,#7aa2c2 22%,#5d7f63 45%,#3f6437 70%,#2f4f2a 100%)}
.hero-wave{left:0;top:600px;width:1200px;height:260px}
.hero-title{left:130px;top:238px;color:#fff;font-family:"Cinzel",serif;font-size:72px;font-weight:400;line-height:1;letter-spacing:1px}
.hero-sub{left:130px;top:398px;color:#fff;font-family:"Cinzel",serif;font-size:27px;line-height:1.25}
.hero-btn{left:131px;top:490px;width:200px;height:52px;background:var(--gold);color:#fff;font-family:"Cinzel",serif;font-size:22px;display:flex;align-items:center;justify-content:center}

/* about */
.about-bg{left:0;top:858px;width:1200px;height:534px;background:var(--pale)}
.about-art{left:40px;top:835px;width:495px;height:357px;border-radius:60% 40% 55% 45%/70% 60% 40% 30%;background:linear-gradient(160deg,#9fbfdd 0%,#cfdceb 40%,#6f8f5b 70%,#4f6b3f 100%);opacity:.85}
.about-title{left:620px;top:860px;color:var(--blue-deep);font-family:"Cinzel",serif;font-size:42px;font-weight:600;line-height:1}
.about-sub{left:620px;top:906px;color:var(--blue-deep);font-family:"Cinzel",serif;font-size:30px;line-height:1}
.about-text{left:620px;top:960px;width:470px;font-size:17px;line-height:1.5;color:var(--muted)}
.about-text p+p{margin-top:14px}
.outline-btn{left:621px;top:1132px;width:169px;height:49px;border:2px solid var(--blue);border-radius:25px;color:var(--blue);font-family:"Montserrat",sans-serif;font-weight:600;font-size:15px;display:flex;align-items:center;justify-content:center}

/* trusted */
.trusted-tab{left:500px;top:1309px;width:200px;height:38px;background:var(--gold);border-radius:20px 20px 0 0;color:#fff;font-family:"Montserrat",sans-serif;font-weight:600;font-size:20px;display:flex;align-items:center;justify-content:center}
.trusted-box{left:159px;top:1344px;width:882px;height:140px;border:2px solid var(--navy);border-radius:70px;background:#fff;display:flex;align-items:center;justify-content:space-around;padding:0 60px}
.partner{display:flex;align-items:center;gap:10px;font-family:"Montserrat",sans-serif;font-size:28px;font-weight:600;color:#555}
.partner i{width:28px;height:28px;background:#666;display:block}

/* services */
.service-card{width:437px;height:209px;border:2px solid #dde0e5;background:#fff}
.service-card h3{position:absolute;left:38px;top:38px;font-family:"Montserrat",sans-serif;font-size:18px;font-weight:700;color:var(--blue-deep)}
.service-card svg{position:absolute;left:42px;top:80px}
.service-card p{position:absolute;left:136px;top:80px;width:280px;font-size:14.5px;line-height:1.35;color:#444}
.service-card a{position:absolute;left:136px;top:154px;font-family:"Montserrat",sans-serif;font-size:14px;font-weight:600;color:var(--blue);text-decoration:underline}

/* solutions */
.solutions-band{left:0;top:2212px;width:1200px;height:618px;background:var(--gold)}
.ring{left:-71px;top:2247px;width:666px;height:666px;border-radius:50%;background:var(--gold-light)}
.traveller{left:-57px;top:2311px;width:600px;height:600px;border-radius:50%;background:linear-gradient(180deg,#4f79b8 0%,#93aed0 45%,#7f8f9a 60%,#5f6d3f 80%,#4d5a2e 100%)}
.sol-title{left:613px;top:2328px;color:#fff;font-family:"Raleway",sans-serif;font-size:36px}
.sol-title b{font-weight:700}
.sol-text{left:613px;top:2392px;width:370px;color:#fff;font-size:13px;line-height:1.5}
.step{left:616px;width:520px;display:flex;gap:26px;align-items:flex-start}
.step-num{width:46px;height:46px;border-radius:50%;background:#a57b32;color:#fff;font-family:"Montserrat",sans-serif;font-weight:700;font-size:17px;display:flex;align-items:center;justify-content:center;flex:none}
.step h4{color:#fff;font-family:"Montserrat",sans-serif;font-weight:500;font-size:18px;margin-top:2px}
.step span{color:#fff;font-size:13px}

/* news */
.news-title{left:0;top:2935px;width:1200px;text-align:center;font-family:"Cinzel",serif;font-size:45px;font-weight:600;color:var(--blue-deep)}
.news-card{top:3027px;width:294px;height:384px;background:#fff;box-shadow:0 4px 14px rgba(0,0,0,.12)}
.news-img{height:174px}
.news-body{padding:26px 32px}
.news-date{font-family:"Montserrat",sans-serif;font-size:14px;font-weight:600;color:var(--blue)}
.news-card h5{font-family:"Montserrat",sans-serif;font-size:15.5px;font-weight:600;color:#222;margin-top:14px;line-height:1.4}
.news-card p{font-size:14px;color:#555;line-height:1.4;margin-top:12px}
.news-more{font-family:"Montserrat",sans-serif;font-size:13.5px;font-weight:600;color:var(--blue);margin-top:14px;display:block}

/* cta */
.cta-title{left:0;top:3490px;width:1200px;text-align:center;font-family:"Montserrat",sans-serif;font-size:33px;font-weight:700;color:var(--blue)}
.cta-sub{left:0;top:3540px;width:1200px;text-align:center;font-size:24px;color:#555;line-height:1.4}
.cta-btn{left:469px;top:3630px;width:243px;height:52px;border-radius:26px;background:var(--blue);color:#fff;font-family:"Montserrat",sans-serif;font-size:20px;font-weight:500;display:flex;align-items:center;justify-content:center}

/* footer */
.site-footer{left:0;top:3739px;width:1200px;height:436px;background:var(--footer);color:#fff}
.foot-head{font-family:"Montserrat",sans-serif;font-size:14px;font-weight:600;color:#fff}
.field{background:#fff;color:#555;font-size:13px;padding:10px 14px;height:36px}
.send-btn{left:131px;top:4029px;width:132px;height:39px;border-radius:20px;background:var(--gold);color:#fff;font-family:"Montserrat",sans-serif;font-weight:600;font-size:16px;display:flex;align-items:center;justify-content:center}
.links{list-style:none;font-size:14px;color:#e6e6e6}
.links li{height:27.5px;display:flex;align-items:center;gap:8px}
.links li::before{content:"»";color:var(--gold)}
.contact-line{display:flex;gap:10px;font-size:13.5px;color:#e6e6e6;line-height:1.4}
.social{width:27px;height:27px;border-radius:50%;background:var(--gold)}
.foot-rule{left:0;top:4112px;width:1200px;height:1px;background:#555c66}
.copyright{left:0;top:4132px;width:1200px;text-align:center;font-size:15px;color:#e0e0e0}
</style>
</head>
<body>

<header class="abs site-header">
  <div class="abs brand"><span class="brand-mark"></span><span class="brand-name">Velmora Kestrel<br>Bridgeworks</span></div>
  <div class="abs call">
    <svg width="44" height="44" viewBox="0 0 44 44"><circle cx="22" cy="22" r="20" fill="none" stroke="#1f5fae" stroke-width="2"/><path d="M15 13c2-1 4 3 4 4s-2 2-1 4 3 4 5 5 3-1 4-1 5 2 4 4-3 3-5 2C19 29 14 23 13 18c0-2 1-4 2-5z" fill="#1f5fae"/></svg>
    <div><div class="call-label">Call Now</div><div class="call-number">1 555 010 2040</div></div>
  </div>
  <div class="abs quote-btn"><svg width="20" height="14" viewBox="0 0 20 14"><rect x="1" y="1" width="18" height="12" fill="none" stroke="#fff" stroke-width="2"/><path d="M1 1l9 7 9-7" fill="none" stroke="#fff" stroke-width="2"/></svg>GET A QUOTE</div>
  <div class="abs menu-btn"><span></span><span></span><span></span></div>
</header>

<section>
  <div class="abs hero-photo" role="img" aria-label="Mountain ridge with an ancient stone wall winding across green hills under a blue sky"></div>
  <svg class="abs hero-wave" viewBox="0 0 1200 260" preserveAspectRatio="none">
    <path d="M0 240 C250 100 450 110 700 130 C900 145 1080 150 1200 40 L1200 260 L0 260 Z" fill="#e8eef7"/>
    <path d="M430 130 C650 95 850 150 1000 140 C1100 132 1170 90 1200 40 L1200 70 C1170 120 1100 155 1000 160 C850 168 650 120 430 130 Z" fill="#b5893b"/>
  </svg>
  <h1 class="abs hero-title">Trust Our<br>Experience</h1>
  <p class="abs hero-sub">Dare to live the life you've<br>always wanted.</p>
  <div class="abs hero-btn">Learn More</div>
</section>

<section>
  <div class="abs about-bg"></div>
  <div class="abs about-art" role="img" aria-label="Fanned wave shapes filled with mountain and sky scenery"></div>
  <h2 class="abs about-title">Velmora Kestrel</h2>
  <div class="abs about-sub">Bridgeworks</div>
  <div class="abs about-text">
    <p>Lorem Ipsum is simply dummy text of the printing and typesetting industry. Lorem Ipsum has been</p>
    <p>industry's standard dummy text ever since the 1500s, when an unknown printer took a galley of type and scrambled Lorem Ipsum is simply dummy</p>
  </div>
  <div class="abs outline-btn">LEARN MORE</div>

  <div class="abs trusted-tab">Trusted By</div>
  <div class="abs trusted-box">
    <div class="partner"><i></i>Northvale</div>
    <div class="partner">Cobrin</div>
    <div class="partner">Asterly</div>
    <div class="partner"><i style="border-radius:50%"></i>Quillon</div>
  </div>
</section>

<section>
  <div class="abs service-card" style="left:151px;top:1622px">
    <h3>TOURISM</h3>
    <svg width="74" height="70" viewBox="0 0 74 70"><circle cx="37" cy="24" r="18" fill="none" stroke="#b5893b" stroke-width="4"/><path d="M25 40l6 12h12l6-12" fill="none" stroke="#b5893b" stroke-width="3"/><rect x="30" y="52" width="14" height="10" fill="#b5893b"/><path d="M2 50h18M54 50h18" stroke="#b5893b" stroke-width="4"/></svg>
    <p>Lorem Ipsum is simply dummy text of the printing and typesetting industry. Lorem Ipsum has been the</p>
    <a>Read More</a>
  </div>
  <div class="abs service-card" style="left:611px;top:1622px">
    <h3>EXPORT OF PRODUCTS</h3>
    <svg width="74" height="70" viewBox="0 0 74 70"><path d="M37 4l16 6v14c0 10-7 16-16 20-9-4-16-10-16-20V10z" fill="none" stroke="#b5893b" stroke-width="4"/><path d="M30 24l5 5 9-10" fill="none" stroke="#b5893b" stroke-width="4"/><path d="M8 36l12 18h8M66 36L54 54h-8" fill="none" stroke="#b5893b" stroke-width="4"/><rect x="20" y="58" width="8" height="8" fill="#b5893b"/><rect x="46" y="58" width="8" height="8" fill="#b5893b"/></svg>
    <p>Lorem Ipsum is simply dummy text of the printing and typesetting industry. Lorem Ipsum has been the</p>
    <a>Read More</a>
  </div>
  <div class="abs service-card" style="left:151px;top:1857px">
    <h3>SERVICES</h3>
    <svg width="74" height="70" viewBox="0 0 74 70"><circle cx="34" cy="34" r="30" fill="none" stroke="#b5893b" stroke-width="5"/><path d="M4 34h60M34 4c-12 14-12 46 0 60M34 4c12 14 12 46 0 60" fill="none" stroke="#b5893b" stroke-width="4"/><path d="M46 40h18l-6-8M64 40l-6 8" fill="none" stroke="#b5893b" stroke-width="5"/></svg>
    <p>Lorem Ipsum is simply dummy text of the printing and typesetting industry. Lorem Ipsum has been the</p>
    <a>Read More</a>
  </div>
  <div class="abs service-card" style="left:611px;top:1857px">
    <h3>INFLUENCER MARKETING</h3>
    <svg width="74" height="70" viewBox="0 0 74 70"><rect x="10" y="4" width="36" height="60" fill="#b5893b"/><path d="M16 16h22M16 26h22M16 36h14M16 46h14" stroke="#fff" stroke-width="3"/><path d="M40 34l18-8v28l-18-8z" fill="#b5893b" stroke="#fff" stroke-width="2"/><path d="M62 32v16" stroke="#b5893b" stroke-width="4"/></svg>
    <p>Lorem Ipsum is simply dummy text of the printing and typesetting industry. Lorem Ipsum has been the</p>
    <a>Read More</a>
  </div>
</section>

<section>
  <div class="abs solutions-band"></div>
  <div class="abs ring"></div>
  <div class="abs traveller" role="img" aria-label="Hiker with a backpack raising his arms on a mountain top at sunrise"></div>
  <h2 class="abs sol-title">Simple <b>Solutions!</b></h2>
  <p class="abs sol-text">The task at hand is challenging since the target group includes people with numerous and different backgrounds in terms of native language.</p>
  <div class="abs step" style="top:2478px"><div class="step-num">1</div><div><h4>Lorem Ipsum is simply dummy</h4><span>Lorem Ipsum is simply dummy text of the printing</span></div></div>
  <div class="abs step" style="top:2551px"><div class="step-num">2</div><div><h4>Lorem Ipsum is simply dummy</h4><span>Lorem Ipsum is simply dummy text</span></div></div>
  <div class="abs step" style="top:2624px"><div class="step-num">3</div><div><h4>Lorem Ipsum is simply dummy</h4><span>Lorem Ipsum is simply dummy text</span></div></div>
</section>

<section>
  <h2 class="abs news-title">Latest News</h2>
  <article class="abs news-card" style="left:131px">
    <div class="news-img" role="img" aria-label="Two travellers with backpacks cheering by a lake" style="background:linear-gradient(180deg,#9cb8d4,#6f8fa8 55%,#4e6270)"></div>
    <div class="news-body"><div class="news-date">JAN 20, 2020</div><h5>INDUSTRY'S STANDARD DUMMY TEXT EVER</h5><p>Lorem Ipsum is simply dummy text of the printing &amp; typesetting industry. Lorem Ipsum</p><span class="news-more">LEARN MORE ›</span></div>
  </article>
  <article class="abs news-card" style="left:452px">
    <div class="news-img" role="img" aria-label="Hiker with a hat reading a map in a forest" style="background:linear-gradient(160deg,#4d6a34,#7b8f52 50%,#3c4e2a)"></div>
    <div class="news-body"><div class="news-date">JAN 20, 2020</div><h5>INDUSTRY'S STANDARD DUMMY TEXT EVER</h5><p>Lorem Ipsum is simply dummy text of the printing &amp; typesetting industry. Lorem Ipsum</p><span class="news-more">LEARN MORE ›</span></div>
  </article>
  <article class="abs news-card" style="left:774px">
    <div class="news-img" role="img" aria-label="Traveller photographing a mountain lake" style="background:linear-gradient(180deg,#6aa0d6,#d5e3ef 35%,#3f5a3c 60%,#2a4a5e)"></div>
    <div class="news-body"><div class="news-date">JAN 20, 2020</div><h5>INDUSTRY'S STANDARD DUMMY TEXT EVER</h5><p>Lorem Ipsum is simply dummy text of the printing &amp; typesetting industry. Lorem Ipsum</p><span class="news-more">LEARN MORE ›</span></div>
  </article>
</section>

<section>
  <h2 class="abs cta-title">Want to know more?</h2>
  <p class="abs cta-sub">Request a free assessment and<br>get started today</p>
  <div class="abs cta-btn">Request A Call</div>
</section>

<footer class="abs site-footer"></footer>
<div class="abs foot-head" style="left:136px;top:3806px">GET IN TOUCH</div>
<div class="abs field" style="left:131px;top:3851px;width:219px">Your kid's name</div>
<div class="abs field" style="left:358px;top:3851px;width:221px">Your kid's age</div>
<div class="abs field" style="left:131px;top:3898px;width:219px">Your Email</div>
<div class="abs field" style="left:358px;top:3898px;width:221px">Phone Number</div>
<div class="abs field" style="left:131px;top:3945px;width:448px;height:71px">Your Message</div>
<div class="abs send-btn">Send Us</div>

<div class="abs foot-head" style="left:649px;top:3806px">QUICK LINKS</div>
<ul class="abs links" style="left:649px;top:3838px"><li>Home</li><li>About</li><li>Blog</li><li>Tourism</li><li>Contact Us</li></ul>

<div class="abs foot-head" style="left:834px;top:3806px">QUICK LINKS</div>
<div class="abs contact-line" style="left:834px;top:3843px"><svg width="14" height="16" viewBox="0 0 14 16"><path d="M7 1a5 5 0 015 5c0 4-5 9-5 9S2 10 2 6a5 5 0 015-5z" fill="none" stroke="#b5893b" stroke-width="1.6"/><circle cx="7" cy="6" r="1.8" fill="#b5893b"/></svg><span>Address, City<br>Home Care Management</span></div>
<div class="abs contact-line" style="left:834px;top:3899px"><svg width="16" height="16" viewBox="0 0 16 16"><path d="M3 1c1 0 3 3 3 4s-1 1-1 2 3 4 4 4 1-1 2-1 4 2 4 3-2 2-3 2C6 15 1 10 1 4c0-1 1-3 2-3z" fill="#b5893b"/></svg><span>(555) 014-2290</span></div>
<div class="abs contact-line" style="left:834px;top:3938px"><svg width="16" height="12" viewBox="0 0 16 12"><rect x="1" y="1" width="14" height="10" fill="none" stroke="#b5893b" stroke-width="1.4"/><path d="M1 1l7 6 7-6" fill="none" stroke="#b5893b" stroke-width="1.4"/></svg><span>hello@velmora.example</span></div>

<div class="abs foot-head" style="left:649px;top:4012px;font-size:13.5px">STAY CONNECTED</div>
<div class="abs social" style="left:799px;top:4005px"></div>
<div class="abs social" style="left:834px;top:4005px"></div>
<div class="abs social" style="left:869px;top:4005px"></div>
<div class="abs social" style="left:904px;top:4005px"></div>

<div class="abs foot-rule"></div>
<div class="abs copyright">© 2020 Velmora Kestrel Bridgeworks | All Rights are Reserved | Terms and Conditions</div>

</body>
</html>
```